Instagram post design for clothing brand

please see the attached design brief PDF

I will raise the budget for designs so I want to provide more submissions and designs
I have extended the deadline for submissions by one week extra

• I want t-shirt mockup so I can put any design I want

```html
<!DOCTYPE html>
<html lang="en">
<head>
<meta charset="utf-8">
<title>KOVRA – Instagram post set</title>
<link rel="stylesheet" href="https://fonts.googleapis.com/css2?family=Bebas+Neue&family=Montserrat:wght@800&family=Open+Sans:wght@400&display=swap">
<style>
  :root{
    --board:#d3d4d6;
    --board-edge:#8a8b8d;
    --brand-blue:#229ad2;
    --paper:#ffffff;
    --paper-shade:#f1f2f3;
    --ink:#0c0c0c;
    --ink-soft:#2f2f2f;
    --ring-track:#eef0f1;
  }
  *{box-sizing:border-box;margin:0;padding:0}
  html,body{width:1200px;height:1037px;overflow:hidden;background:var(--board)}
  .board{position:relative;width:1200px;height:1037px;background:var(--board);border:1px solid var(--board-edge)}
  .post{position:absolute;width:360px;height:360px;overflow:hidden;background:var(--brand-blue)}
  .post--loading{left:39px;top:316px}
  .post--product{left:424px;top:322px}
  .post--sale{left:809px;top:318px}
  .post__art{position:absolute;inset:0;width:360px;height:360px}
  .torn{fill:var(--paper);filter:drop-shadow(0 3px 3px rgba(0,40,70,.35))}
  .torn--bottom{filter:drop-shadow(0 -3px 3px rgba(0,40,70,.35))}

  .wordmark{position:absolute;font-family:"Bebas Neue",sans-serif;line-height:1;letter-spacing:.5px;text-align:center}
  .wordmark__square{display:block;margin:0 auto 4px}

  .loading__brand{left:143px;top:146px;width:100px;color:var(--paper);font-size:24px}
  .loading__brand .wordmark__square{width:40px;height:40px;background:var(--paper)}
  .loading__label{position:absolute;left:0;width:390px;top:280px;text-align:center;font-family:"Montserrat",sans-serif;font-weight:800;font-size:19px;letter-spacing:2px;color:var(--ink-soft)}

  .product__photo{position:absolute;left:59px;top:37px;width:206px;height:292px;border-radius:40px 40px 6px 6px;background:linear-gradient(90deg,#c9977a 0%,#141414 14%,#0b0b0b 50%,#141414 86%,#c9977a 100%)}
  .product__brand{left:290px;top:26px;width:54px;color:var(--brand-blue);font-size:17px}
  .product__brand .wordmark__square{width:30px;height:34px;background:var(--ink)}
  .product__price{position:absolute;left:285px;top:192px;font-family:"Bebas Neue",sans-serif;font-size:22px;color:var(--paper)}
  .sizes{position:absolute;left:183px;top:329px;display:flex;align-items:center;gap:6px;font-family:"Open Sans",sans-serif;color:var(--ink-soft)}
  .sizes__label{font-size:13px;margin-right:14px}
  .sizes__option{width:17px;height:17px;border:1px solid var(--ink-soft);border-radius:50%;font-size:7px;display:flex;align-items:center;justify-content:center}

  .sale__shirts{position:absolute;left:8px;top:34px;width:336px;height:218px;border-radius:28px 28px 60px 20px;background:linear-gradient(160deg,#151515,#050505)}
  .sale__offer{position:absolute;left:117px;top:170px;font-family:"Bebas Neue",sans-serif;font-size:62px;line-height:1;color:var(--paper);letter-spacing:1px}
  .sale__brand{left:22px;top:296px;width:28px;color:var(--paper);font-size:10px}
  .sale__brand .wordmark__square{width:20px;height:22px;background:var(--paper);margin-bottom:2px}
  .social{fill:var(--paper)}
</style>
</head>
<body>
<main class="board">

  <section class="post post--loading">
    <svg class="post__art" viewBox="0 0 360 360" aria-hidden="true">
      <defs>
        <linearGradient id="ringFill" x1="120" y1="260" x2="270" y2="110" gradientUnits="userSpaceOnUse">
          <stop offset="0" stop-color="#2b2b2b"/>
          <stop offset=".55" stop-color="#8c8c8c"/>
          <stop offset="1" stop-color="#e2e2e2"/>
        </linearGradient>
      </defs>
      <path class="torn" d="M0,0H360V64L352,66 342,70 330,72 320,80 310,76 300,80 290,82 278,86 268,88 260,86 250,80 240,72 230,68 222,62 214,60 206,58 200,64 196,56 190,62 186,56 178,58 172,62 164,66 158,72 150,74 142,72 134,70 128,76 120,78 112,80 104,86 96,90 88,98 80,100 72,106 62,115 52,118 46,128 38,120 30,110 22,112 12,104 0,107Z"/>
      <path class="torn torn--bottom" d="M0,335L20,332 40,328 60,330 80,326 100,324 120,320 140,322 160,318 180,320 200,316 220,318 240,312 260,314 280,308 300,306 320,300 340,306 360,308V360H0Z"/>
      <circle cx="193" cy="186" r="82" fill="none" stroke="var(--paper)" stroke-width="1.5"/>
      <circle cx="193" cy="186" r="70" fill="none" stroke="var(--ring-track)" stroke-width="22"/>
      <circle cx="193" cy="186" r="70" fill="none" stroke="url(#ringFill)" stroke-width="22" stroke-dasharray="329.9 439.8" transform="rotate(90 193 186)"/>
      <circle cx="193" cy="186" r="58" fill="none" stroke="var(--paper)" stroke-width="1.5"/>
    </svg>
    <div class="wordmark loading__brand"><span class="wordmark__square"></span>KOVRA</div>
    <p class="loading__label">LOADING 75%</p>
  </section>

  <section class="post post--product">
    <svg class="post__art" viewBox="0 0 360 360" aria-hidden="true">
      <path class="torn" d="M0,0H360V104L350,106 340,112 330,114 320,124 312,118 304,110 296,100 288,92 280,90 272,84 264,82 256,76 248,70 240,66 230,62 220,60 210,58 200,56 190,50 180,44 170,42 160,40 150,42 140,46 120,50 110,56 100,58 90,62 80,64 70,66 60,60 50,58 40,54 30,50 20,48 10,42 0,38Z"/>
      <path class="torn torn--bottom" d="M0,334L14,330 28,332 40,326 56,328 70,324 90,322 110,320 130,318 150,318 170,316 190,316 210,314 230,316 250,312 270,306 290,302 310,302 330,298 345,296 360,300V360H0Z"/>
      <circle class="social" cx="342" cy="224" r="3.5"/>
      <circle class="social" cx="342" cy="232" r="3.5"/>
      <circle class="social" cx="342" cy="240" r="3.5"/>
      <circle class="social" cx="342" cy="249" r="3.5"/>
    </svg>
    <div class="product__photo" role="img" aria-label="Model wearing a black crew-neck t-shirt with the KOVRA print"></div>
    <div class="wordmark product__brand"><span class="wordmark__square"></span>KOVRA</div>
    <p class="product__price">19.990 KD</p>
    <div class="sizes">
      <span class="sizes__label">size</span>
      <span class="sizes__option">S</span>
      <span class="sizes__option">M</span>
      <span class="sizes__option">L</span>
      <span class="sizes__option">XL</span>
      <span class="sizes__option">XXL</span>
    </div>
  </section>

  <section class="post post--sale">
    <svg class="post__art" viewBox="0 0 360 360" aria-hidden="true">
      <path class="torn" d="M0,0H360V48L340,50 320,48 300,42 280,40 260,38 240,34 220,32 200,30 180,30 160,28 140,26 120,30 100,28 80,24 60,22 40,26 20,22 10,28 0,26Z"/>
      <path class="torn torn--bottom" d="M0,360L10,340 20,336 30,330 40,334 50,340 60,344 70,350 90,354 120,356 150,358 180,358 210,356 240,354 260,346 270,340 280,320 290,314 300,312 310,318 318,312 330,314 345,318 360,316V360Z"/>
      <circle class="social" cx="68" cy="306" r="6"/>
      <circle class="social" cx="68" cy="322" r="6"/>
      <circle class="social" cx="169" cy="306" r="6"/>
      <circle class="social" cx="169" cy="322" r="6"/>
    </svg>
    <div class="sale__shirts" role="img" aria-label="Two black t-shirts with the KOVRA print, laid at an angle"></div>
    <p class="sale__offer">50% OFF</p>
    <div class="wordmark sale__brand"><span class="wordmark__square"></span>KOVRA</div>
  </section>

</main>
</body>
</html>
```